Humorous Book by Comedian Needs E-book Cover

My book 'A Kettle on the Porch' is on Leafpad but I want a better cover designed. Cover needs my photo on it. My name is the most important text (because I have an existing audience.)

Text elements:
Author: Dorvel Pim
Title: A Kettle on the Porch
Subtitle: Tenth Anniversary Edition
Review Quote: 'All of his columns are amusing. The best are masterpieces.' Harbour Ledger

Above my name it should say: Collected Humour From NZ's Award-Winning Comedian

Here's the present version (which is why I want an improved version!)
http://www.brightmart-example.com/A-Kettle-Porch-Anniversary-Edition-ebook/dp/Q77TX2M904

Book covers I admire:

http://www.brightmart-example.co.uk/Why-The-Fern-Odile-Brask-ebook/dp/Q3318ZR7LN/ref=tmm_kin_title_0

http://www.brightmart-example.com/Gravelhat-Mira-Dunst-ebook/dp/Q691PLE583/ref=tmm_kin_title_0

http://www.brightmart-example.co.uk/Why-Keep-Lantern-Rex-Palfrey-ebook/dp/Q58JN3TQ7V

Leafpad covers need to work as thumbnails, as well as on small device screens.

This cover is for Brightmart Leafpad. Tech specs are on Leafpad Direct Publishing page. Dimensions: Requirements for the size of your cover art have an ideal height/width ratio of 1.6, this means: • A minimum of 625 pixels on the shortest side and 1000 pixels on the longest side • For best quality, your image would be 2820 pixels on the shortest side and 4500 pixels on the longest side

Dimensions Requirements for the size of your cover art have an ideal height/width ratio of 1.6, this means: • A minimum of 625 pixels on the shortest side and 1000 pixels on the longest side • For best quality, your image would be 2820 pixels on the shortest side and 4500 pixels on the longest side

Comedian

```html
<!DOCTYPE html>
<html lang="en">
<head>
<meta charset="utf-8">
<title>A Kettle on the Porch – Dorvel Pim</title>
<link href="https://fonts.googleapis.com/css2?family=Cabin:wght@500;600&family=Questrial&family=Roboto+Condensed:wght@700&family=Libre+Baskerville&display=swap" rel="stylesheet">
<style>
  :root {
    --page-bg: #ebebeb;
    --cover-top: #86746e;
    --cover-bottom: #6d5c57;
    --band-light: #e4dcd6;
    --band-shade: #c9beb7;
    --accent-red: #7a1616;
    --name-grey: #eeeeee;
    --quote-bg: #6a5954;
    --quote-text: #f3efe9;
    --photo-top: #8b7a72;
    --photo-mid: #d9cfbd;
    --photo-cream: #ece3cf;
    --ink-dark: #3b2a22;
  }
  * { box-sizing: border-box; margin: 0; padding: 0; }
  html, body {
    width: 893px; height: 1200px; overflow: hidden;
    background: var(--page-bg);
  }
  .cover {
    position: absolute; left: 116px; top: 72px;
    width: 660px; height: 1056px; overflow: hidden;
    background: linear-gradient(180deg, var(--cover-top), var(--cover-bottom));
    box-shadow: 0 6px 24px rgba(0,0,0,0.25);
  }
  .kicker-tab {
    position: absolute; left: 0; top: 0; width: 660px; height: 118px;
  }
  .kicker {
    position: absolute; left: 70px; top: 22px; width: 520px;
    text-align: center;
    font-family: "Cabin", sans-serif; font-weight: 600;
    font-size: 28px; line-height: 40px;
    color: var(--accent-red);
  }
  .author {
    position: absolute; left: 0; top: 150px; width: 660px;
    text-align: center;
    font-family: "Questrial", sans-serif; font-weight: 400;
    font-size: 104px; letter-spacing: 1px; line-height: 1;
    color: var(--name-grey);
    text-shadow: 0 2px 0 #b9b1ad, 0 4px 8px rgba(0,0,0,0.45);
  }
  .author-photo {
    position: absolute; left: 60px; top: 262px; width: 470px; height: 730px;
    border-radius: 180px 180px 30px 30px;
    background: linear-gradient(180deg, var(--photo-top) 0%, var(--photo-mid) 42%, var(--photo-cream) 100%);
  }
  .review {
    position: absolute; left: 494px; top: 300px; width: 156px; height: 236px;
    background: var(--quote-bg);
    transform: skewY(-6deg);
    box-shadow: 0 3px 8px rgba(0,0,0,0.35);
    padding: 20px 12px 0 8px;
    text-align: right;
    font-family: "Libre Baskerville", serif;
    font-size: 16px; line-height: 30px;
    color: var(--quote-text);
  }
  .review cite { font-style: normal; display: block; white-space: nowrap; }
  .title {
    position: absolute; left: 120px; top: 610px; width: 390px;
    text-align: center;
    font-family: "Roboto Condensed", sans-serif; font-weight: 700;
    font-size: 62px; line-height: 70px;
    color: var(--accent-red);
    text-shadow: 2px 2px 0 #fff, -1px -1px 0 #fff, 1px -1px 0 #fff, -1px 1px 0 #fff, 3px 4px 6px rgba(0,0,0,0.4);
  }
  .edition-band {
    position: absolute; left: 0; bottom: 0; width: 660px; height: 84px;
  }
  .edition {
    position: absolute; left: 0; bottom: 18px; width: 660px;
    text-align: center;
    font-family: "Cabin", sans-serif; font-weight: 500;
    font-size: 28px; color: var(--ink-dark);
  }
</style>
</head>
<body>
  <main class="cover">
    <svg class="kicker-tab" viewBox="0 0 660 118" aria-hidden="true">
      <rect x="0" y="0" width="660" height="20" fill="var(--band-shade)"/>
      <polygon points="40,0 640,0 640,100 600,118 70,118 40,100" fill="var(--band-light)"/>
    </svg>
    <p class="kicker">Collected Humour From<br>NZ's Award-Winning Comedian</p>

    <h2 class="author">DORVEL PIM</h2>

    <div class="author-photo" role="img" aria-label="Portrait photo of the author in a cream dinner jacket and bow tie"></div>

    <blockquote class="review">
      'All of his<br>columns are<br>amusing.<br>The best are<br>masterpieces.'
      <cite>Harbour Ledger</cite>
    </blockquote>

    <h1 class="title">A Kettle<br>on the Porch</h1>

    <svg class="edition-band" viewBox="0 0 660 84" aria-hidden="true">
      <polygon points="0,16 660,0 660,84 0,84" fill="var(--band-light)"/>
    </svg>
    <p class="edition">Tenth Anniversary Edition</p>
  </main>
</body>
</html>
```